Advertisement Sign Project

Hi there,

I have a commercial space available for short term lease.

I need an advertisement sign to go on the double black doors (under the current Bornavel Quindrex sign).

The advertising sign should be about A3 in size and designed to attract pedestrians.

See site address at 417 Calder Parade Richmond Victoria Australia:

https://plotfinder.example-atlas.com.au/view?q=417B+Calder+Pde,+Richmond+Victoria+3121&z=17

Target Market(s)

Pop-up store tenants: fashion, textiles, bedding, furniture, homewares and kitchenwares.

The photos are provided to give you (the graphic designer) an idea of the space available.

Requirements
Must have
• Retail tenancy available for short term lease.

For all enquiries contact Owen - 0412730648 or email owen@calderparadehub.com.au

Nice to have
• Something befitting the look and feel of the building.

I was thinking a textile pattern as background, or some kind of fashion design element to inspire a potential pop up shop tenant.

```html
<!DOCTYPE html>
<html lang="en">
<head>
<meta charset="utf-8">
<title>Retail Tenancy – Short Term Lease Sign</title>
<link rel="stylesheet" href="https://fonts.googleapis.com/css2?family=Anton&family=Arimo:wght@700&family=PT+Serif:wght@700&family=Righteous&display=swap">
<style>
  :root {
    --sky-yellow: #f4e92c;
    --sky-mid: #d5e0b8;
    --sky-blue: #a3c0e8;
    --band-light: #fbf8c6;
    --band-strong: #f6e81c;
    --floor-blue-top: #7aa3de;
    --floor-blue-bottom: #4f7cc9;
    --ink: #111111;
    --paper: #ffffff;
    --lease-yellow: #f7e74a;
    --lease-edge: #3b3a1c;
    --at-yellow: #f2d400;
  }
  html, body {
    margin: 0;
    padding: 0;
    width: 1200px;
    height: 1000px;
    overflow: hidden;
    background: var(--paper);
  }
  .sign {
    display: block;
    width: 1200px;
    height: 1000px;
  }
  .outlined {
    paint-order: stroke fill;
    stroke-linejoin: round;
  }
  .headline {
    font-family: "Anton", "Impact", sans-serif;
    font-size: 140px;
    fill: var(--paper);
    stroke: var(--ink);
    stroke-width: 16px;
  }
  .subhead {
    font-family: "Righteous", "Arial Rounded MT Bold", sans-serif;
    font-size: 104px;
    fill: var(--lease-yellow);
    stroke: var(--lease-edge);
    stroke-width: 7px;
  }
  .tagline {
    font-family: "Anton", "Impact", sans-serif;
    font-size: 60px;
    fill: var(--paper);
    stroke: var(--ink);
    stroke-width: 9px;
  }
  .call {
    font-family: "Arimo", "Arial", sans-serif;
    font-weight: 700;
    font-size: 118px;
    fill: var(--ink);
    stroke: var(--paper);
    stroke-width: 16px;
  }
  .at-mark {
    font-family: "Arimo", "Arial", sans-serif;
    font-weight: 700;
    font-size: 104px;
    fill: var(--at-yellow);
    stroke: #2c2c2c;
    stroke-width: 4px;
  }
  .address {
    font-family: "PT Serif", "Georgia", serif;
    font-weight: 700;
    font-size: 62px;
    fill: var(--paper);
    stroke: var(--ink);
    stroke-width: 9px;
  }
  .enquiry {
    font-family: "Arimo", "Arial", sans-serif;
    font-weight: 700;
    font-size: 32px;
    fill: var(--ink);
  }
</style>
</head>
<body>
<svg class="sign" viewBox="0 0 1200 1000" xmlns="http://www.w3.org/2000/svg">
  <defs>
    <linearGradient id="sky" x1="0" y1="0" x2="0" y2="1">
      <stop offset="0" stop-color="var(--sky-yellow)"/>
      <stop offset="0.45" stop-color="var(--sky-mid)"/>
      <stop offset="1" stop-color="var(--sky-blue)"/>
    </linearGradient>
    <linearGradient id="band" x1="0" y1="0" x2="0" y2="1">
      <stop offset="0" stop-color="var(--band-light)"/>
      <stop offset="1" stop-color="var(--band-strong)"/>
    </linearGradient>
    <linearGradient id="floor" x1="0" y1="0" x2="0" y2="1">
      <stop offset="0" stop-color="var(--floor-blue-top)"/>
      <stop offset="1" stop-color="var(--floor-blue-bottom)"/>
    </linearGradient>
  </defs>

  <rect class="backdrop" x="0" y="0" width="1200" height="716" fill="url(#sky)"/>

  <text class="headline outlined" x="48" y="152" textLength="1100" lengthAdjust="spacingAndGlyphs">COMERCIAL SPACE AVAILABLE</text>
  <text class="subhead outlined" x="215" y="258" textLength="770" lengthAdjust="spacingAndGlyphs">for short term lease</text>
  <text class="tagline outlined" x="95" y="352" textLength="1015" lengthAdjust="spacingAndGlyphs">Retail tenancy available for short term lease</text>
  <text class="call outlined" x="85" y="494" textLength="1025" lengthAdjust="spacingAndGlyphs">CALL # 0412730648</text>
  <text class="at-mark outlined" x="575" y="598" text-anchor="middle">@</text>
  <text class="address outlined" x="25" y="683" textLength="1155" lengthAdjust="spacingAndGlyphs">417 Calder Parade Richmond Victoria Australia</text>

  <rect class="contact-band" x="0" y="716" width="1200" height="118" fill="url(#band)"/>
  <text class="enquiry" x="57" y="763" textLength="1078" lengthAdjust="spacingAndGlyphs">For all enquiries contact Owen - 0412730648 or email</text>
  <text class="enquiry" x="600" y="803" text-anchor="middle">owen@calderparadehub.com.au</text>

  <rect class="footwear-illustration" x="0" y="834" width="1200" height="166" fill="url(#floor)" role="img" aria-label="Illustration of three stylised high-heeled shoes in black and white on a blue tiled floor"/>
</svg>
</body>
</html>
```